Website for "Bright Meadow Ltd" cleaning bsuiness

We require a website to expose our business to the local market. We want to provide background on who we are and what we do but in an easily digestible way. We clean domestic and commercial premises and want to provide a list of all of our services to potential customers. We operate out of Warrington in the UK.

We would like the website to be animated in some way so that the experience of using it is not dull or mundane. This website needs to be an extension of our company.

Target Market(s)

30 - 60 year olds for Domestic plus commercial clients

Industry/Entity Type

Cleaning Service

Coding

Coded - Design and coding required

Number of Pages Required

4 page

Font styles to use
Sans Serif

Colors
0455a3
3176b5
85acd3
cfdeed
ffffff
000000
1b1b1b
c8c8c8
757575

Requirements
Must have
• Logo which has been provided. Theme based around the logo and its colours. Simple layout to avoid confusion.
Nice to have
• Animations where possible to impress the customer.
Should not have
• any pictures of cleaning equipment, fairies, maids etc

```html
<!DOCTYPE html>
<html lang="en">
<head>
<meta charset="utf-8">
<title>Bright Meadow Ltd — Professional Cleaning Service</title>
<link href="https://fonts.googleapis.com/css2?family=Raleway:wght@300;400;500;600&display=swap" rel="stylesheet">
<style>
:root{
  --blue:#0455a3;
  --blue-mid:#3176b5;
  --blue-light:#85acd3;
  --blue-pale:#cfdeed;
  --white:#ffffff;
  --black:#000000;
  --ink:#1b1b1b;
  --line:#c8c8c8;
  --grey:#757575;
  --footer:#222222;
}
*{margin:0;padding:0;box-sizing:border-box}
html,body{width:1200px;height:2995px;overflow:hidden}
body{font-family:'Raleway',sans-serif;color:var(--ink);background:var(--white);position:relative}
.abs{position:absolute}

/* top bar + header */
.topbar{left:0;top:0;width:1200px;height:28px;background:var(--blue)}
.topbar-phone{right:58px;top:6px;color:var(--white);font-size:12px;font-weight:500;display:flex;align-items:center;gap:6px}
.header{left:0;top:28px;width:1200px;height:92px;background:var(--white)}
.brand-card{left:60px;top:0;width:224px;height:150px;background:var(--white);box-shadow:0 2px 10px rgba(0,0,0,.25);border-radius:0 0 6px 6px;z-index:5;display:flex;align-items:center;justify-content:center;gap:10px;padding:0 14px}
.brand-mark{width:18px;height:18px;background:var(--blue);flex:none}
.brand-name{color:var(--blue);font-weight:600;font-size:22px;line-height:1.15}
.nav{right:58px;top:80px;display:flex;gap:30px}
.nav a{color:var(--blue);text-decoration:none;font-size:15px;font-weight:500;letter-spacing:.3px}

/* hero */
.hero{left:0;top:120px;width:1200px;height:640px;overflow:hidden}
.hero-photo{position:absolute;inset:0;background:linear-gradient(180deg,#3e3b38 0%,#54463a 55%,#6a5340 100%)}
.hero-shape{position:absolute;left:0;top:0}
.hero-content{position:absolute;left:0;top:180px;width:1200px;text-align:center;color:var(--white)}
.hero-title{font-size:27px;font-weight:400;letter-spacing:.5px;margin-top:24px}
.hero-text{font-size:13px;line-height:28px;margin-top:10px}
.btn{display:inline-flex;align-items:center;gap:8px;background:var(--blue);color:var(--white);font-family:inherit;font-size:15px;text-decoration:none;border:0}
.hero .btn{margin-top:18px;height:38px;padding:0 14px}

/* section headings */
.section-title{left:0;width:1200px;text-align:center;font-size:43px;font-weight:300;color:var(--black);letter-spacing:1px}
.about-text{left:150px;top:908px;width:900px;text-align:center;font-size:13px;line-height:31px;color:var(--grey)}
.about-btn{left:516px;top:1118px;width:170px;height:42px;justify-content:center;font-size:17px}

/* services */
.service{width:360px;height:230px;text-align:center;padding-top:28px}
.service--active{background:var(--blue-mid);color:var(--white)}
.service-icon{height:24px;display:flex;justify-content:center}
.service-title{font-size:17px;font-weight:400;margin-top:12px;letter-spacing:.3px}
.service-text{font-size:12.5px;line-height:24px;margin:14px auto 0;width:320px;color:var(--ink)}
.service--active .service-text{color:var(--white)}

/* quote form */
.quote{left:0;top:1826px;width:1200px;height:566px}
.quote-photo{position:absolute;inset:0;background:linear-gradient(180deg,#3a3633 0%,#4c4036 60%,#5e4a3a 100%)}
.quote-title{left:468px;top:110px;width:676px;text-align:center;color:var(--white);font-size:44px;font-weight:300;letter-spacing:.5px}
.quote-sub{left:468px;top:172px;width:676px;text-align:center;color:var(--white);font-size:11px;font-weight:600}
.field{background:var(--white);color:#999;font-size:11px;padding:0 18px;display:flex;align-items:center}
.field--area{align-items:flex-start;padding-top:14px}
.quote-submit{left:744px;top:436px;width:106px;height:36px;justify-content:center;font-size:13px}

/* partners */
.partner{width:156px;height:86px;border:1px solid #eeeeee;display:flex;align-items:center;justify-content:center}
.partner-badge{width:70px;height:26px;background:var(--line);border-radius:3px}

/* footer */
.footer{left:0;top:2586px;width:1200px;height:338px;background:var(--footer);color:var(--white)}
.footer-title{font-size:20px;font-weight:400;letter-spacing:.3px}
.footer-brand{font-size:19px;font-weight:600;color:var(--white);display:flex;align-items:center;gap:8px}
.footer-brand span.sq{width:12px;height:12px;background:var(--white)}
.footer-text{font-size:13px;line-height:26px}
.footer-links{list-style:none;font-size:13px}
.footer-links li{height:33px;display:flex;align-items:center;gap:8px}
.social{display:flex;gap:20px}
.social span{width:12px;height:12px;border-radius:50%;background:#bbbbbb}
.office li{list-style:none;height:33px;display:flex;align-items:center;gap:14px;font-size:13px}
.copyright{left:0;top:2924px;width:1200px;height:71px;background:var(--blue);color:var(--white);font-size:12px;display:flex;align-items:center;justify-content:center}
</style>
</head>
<body>

<div class="abs topbar"></div>
<div class="abs topbar-phone">
  <svg width="12" height="12" viewBox="0 0 24 24"><path fill="#fff" d="M6.6 10.8a15 15 0 0 0 6.6 6.6l2.2-2.2a1 1 0 0 1 1-.25 11.4 11.4 0 0 0 3.6.6 1 1 0 0 1 1 1V20a1 1 0 0 1-1 1A17 17 0 0 1 3 4a1 1 0 0 1 1-1h3.5a1 1 0 0 1 1 1c0 1.25.2 2.45.6 3.6a1 1 0 0 1-.25 1z"/></svg>
  0800 555 0142
</div>
<header class="abs header"></header>
<div class="abs brand-card"><span class="brand-mark"></span><span class="brand-name">Bright Meadow Ltd</span></div>
<nav class="abs nav">
  <a href="#">HOME</a><a href="#">ABOUT US</a><a href="#">SERVICES</a><a href="#">GALLERY</a><a href="#">LOG</a><a href="#">CONTACT US</a>
</nav>

<section class="abs hero">
  <div class="hero-photo" role="img" aria-label="Photograph of cleaning supplies on a wooden floor, darkened"></div>
  <svg class="hero-shape" width="1200" height="640" viewBox="0 0 1200 640">
    <polygon points="0,446 600,640 1200,446 1200,640 0,640" fill="#ffffff"/>
    <path d="M524 640 Q600 570 676 640 Z" fill="#0455a3"/>
    <circle cx="578" cy="620" r="5" fill="#1b1b1b"/>
    <circle cx="600" cy="620" r="6" fill="#ffffff"/>
    <circle cx="622" cy="620" r="5" fill="#1b1b1b"/>
  </svg>
  <div class="hero-content">
    <svg width="60" height="60" viewBox="0 0 60 60"><circle cx="30" cy="30" r="26" fill="none" stroke="#fff" stroke-width="4"/></svg>
    <h1 class="hero-title">HIGH QUALITY CLEANING SERVICES &amp; AFFORDABLE PRICE</h1>
    <p class="hero-text">Lorem ipsum dolor sit amet conse ctetur adipisicing elit, sed do eiusmod tempor incididunt ut labore et<br>dolore magna aliqua. Ut enim ad minim veniam.</p>
    <a class="btn" href="#"><svg width="10" height="10" viewBox="0 0 10 10"><path d="M3 1l4 4-4 4" fill="none" stroke="#fff" stroke-width="1.6"/></svg>Read More</a>
  </div>
</section>

<h2 class="abs section-title" style="top:838px">WHO WE ARE</h2>
<p class="abs about-text">Perspiciatis unde omnis iste natus error sit voluptatem accusantium doloremque laudantium, totam rem aperiam, eaque ipsa. Labore et dolore magnam aliquam quaerat voluptatem. Architecto beatae vitae dicta sunt explicabo. Nemo enim ipsam voluptatem quia voluptas sit aspernatur aut odit aut fugit, sed quia consequuntur magni dolores eos qui ratione voluptatem sequi nesciunt. Perspiciatis unde omnis iste natus error sit voluptatem accusantium doloremque laudantium, totam rem aperiam, eaque ipsa. Labore et dolore magnam aliquam quaerat voluptatem. Architecto beatae vitae dicta sunt explicabo. Nemo enim ipsam voluptatem quia voluptas sit aspernatur aut odit aut fugit, sed quia consequuntur magni dolores eos qui ratione voluptatem sequi nesciunt.</p>
<a class="abs btn about-btn" href="#"><svg width="11" height="11" viewBox="0 0 10 10"><path d="M3 1l4 4-4 4" fill="none" stroke="#fff" stroke-width="1.6"/></svg>READ MORE</a>

<h2 class="abs section-title" style="top:1236px">WHAT WE DO</h2>

<div class="abs service" style="left:60px;top:1326px">
  <div class="service-icon"><svg width="22" height="22" viewBox="0 0 22 22"><path d="M4 7h14l-2 13H6z" fill="#0455a3"/><path d="M6 7a5 5 0 0 1 10 0" fill="none" stroke="#0455a3" stroke-width="1.5"/></svg></div>
  <h3 class="service-title">HOME &amp; FLOOR CLEANING</h3>
  <p class="service-text">Lorem Ipsum is simply dummy text of the printing and typesetting industry. Lorem Ipsum has been the industry's standard dummy text ever since the 1500s, when an unknown printer</p>
</div>
<div class="abs service service--active" style="left:420px;top:1326px">
  <div class="service-icon"><svg width="22" height="22" viewBox="0 0 22 22"><rect x="2" y="2" width="18" height="18" fill="none" stroke="#fff" stroke-width="2"/><path d="M11 2v18M2 11h18" stroke="#fff" stroke-width="2"/></svg></div>
  <h3 class="service-title">WINDOW BUILDING CLEANING</h3>
  <p class="service-text">Lorem Ipsum is simply dummy text of the printing and typesetting industry. Lorem Ipsum has been the industry's standard dummy text ever since the 1500s, when an unknown printer</p>
</div>
<div class="abs service" style="left:780px;top:1326px">
  <div class="service-icon"><svg width="22" height="22" viewBox="0 0 22 22"><rect x="6" y="9" width="9" height="12" rx="1" fill="#0455a3"/><rect x="8" y="4" width="5" height="5" fill="#0455a3"/><path d="M13 5h5" stroke="#0455a3" stroke-width="2"/></svg></div>
  <h3 class="service-title">WOODEN FLOOR CLEANING</h3>
  <p class="service-text">Lorem Ipsum is simply dummy text of the printing and typesetting industry. Lorem Ipsum has been the industry's standard dummy text ever since the 1500s, when an unknown printer</p>
</div>
<div class="abs service" style="left:60px;top:1566px">
  <div class="service-icon"><svg width="26" height="22" viewBox="0 0 26 22"><path d="M3 10l3-6h14l3 6v8H3z" fill="#0455a3"/><circle cx="8" cy="18" r="2.5" fill="#fff"/><circle cx="18" cy="18" r="2.5" fill="#fff"/></svg></div>
  <h3 class="service-title">VEHICLE CLEANING</h3>
  <p class="service-text">Lorem Ipsum is simply dummy text of the printing and typesetting industry. Lorem Ipsum has been the industry's standard dummy text ever since the 1500s, when an unknown printer</p>
</div>
<div class="abs service" style="left:420px;top:1566px">
  <div class="service-icon"><svg width="22" height="22" viewBox="0 0 22 22"><path d="M19 2L10 13" stroke="#0455a3" stroke-width="2"/><path d="M10 13l-7 2 3 5 6-4z" fill="#0455a3"/></svg></div>
  <h3 class="service-title">COMMERCIAL CLEANING</h3>
  <p class="service-text">Lorem Ipsum is simply dummy text of the printing and typesetting industry. Lorem Ipsum has been the industry's standard dummy text ever since the 1500s, when an unknown printer</p>
</div>
<div class="abs service" style="left:780px;top:1566px">
  <div class="service-icon"><svg width="22" height="22" viewBox="0 0 22 22"><rect x="4" y="12" width="14" height="8" fill="#0455a3"/><rect x="9" y="3" width="4" height="8" fill="#0455a3"/></svg></div>
  <h3 class="service-title">MAINTENANCE SERVICE</h3>
  <p class="service-text">Lorem Ipsum is simply dummy text of the printing and typesetting industry. Lorem Ipsum has been the industry's standard dummy text ever since the 1500s, when an unknown printer</p>
</div>

<section class="abs quote">
  <div class="quote-photo" role="img" aria-label="Photograph of cleaning supplies on a wooden floor, darkened"></div>
  <h2 class="abs quote-title">GET NEW FREE SERVICE NOW</h2>
  <p class="abs quote-sub">RECEIVE PROMOTION &amp; GOOD SERVICE FROM US.</p>
  <div class="abs field" style="left:468px;top:242px;width:320px;height:50px">Email Address</div>
  <div class="abs field" style="left:812px;top:242px;width:330px;height:50px">Phone No</div>
  <div class="abs field field--area" style="left:468px;top:308px;width:674px;height:112px">Write Message</div>
  <a class="abs btn quote-submit" href="#"><svg width="10" height="10" viewBox="0 0 10 10"><path d="M3 1l4 4-4 4" fill="none" stroke="#fff" stroke-width="1.6"/></svg>SUBMIT</a>
</section>

<div class="abs partner" style="left:60px;top:2444px"><span class="partner-badge"></span></div>
<div class="abs partner" style="left:246px;top:2444px"><span class="partner-badge"></span></div>
<div class="abs partner" style="left:432px;top:2444px"><span class="partner-badge"></span></div>
<div class="abs partner" style="left:618px;top:2444px"><span class="partner-badge"></span></div>
<div class="abs partner" style="left:804px;top:2444px"><span class="partner-badge"></span></div>
<div class="abs partner" style="left:990px;top:2444px"><span class="partner-badge"></span></div>

<footer class="abs footer">
  <h4 class="abs footer-title" style="left:60px;top:50px">ABOUT BRIGHT MEADOW</h4>
  <div class="abs footer-brand" style="left:60px;top:98px"><span class="sq"></span>Bright Meadow Ltd</div>
  <p class="abs footer-text" style="left:60px;top:176px;width:320px">Lorem Ipsum is simply dummy text of the printing and typesetting industry. Lorem Ipsum has been the industry's standard dummy text .</p>
  <div class="abs social" style="left:60px;top:260px"><span></span><span></span><span></span><span></span><span></span><span></span></div>

  <h4 class="abs footer-title" style="left:420px;top:50px">INFORMATION</h4>
  <ul class="abs footer-links" style="left:420px;top:96px">
    <li><svg width="8" height="8" viewBox="0 0 10 10"><path d="M3 1l4 4-4 4" fill="none" stroke="#fff" stroke-width="1.6"/></svg>Home</li>
    <li><svg width="8" height="8" viewBox="0 0 10 10"><path d="M3 1l4 4-4 4" fill="none" stroke="#fff" stroke-width="1.6"/></svg>About Us</li>
    <li><svg width="8" height="8" viewBox="0 0 10 10"><path d="M3 1l4 4-4 4" fill="none" stroke="#fff" stroke-width="1.6"/></svg>News</li>
    <li><svg width="8" height="8" viewBox="0 0 10 10"><path d="M3 1l4 4-4 4" fill="none" stroke="#fff" stroke-width="1.6"/></svg>Contact Us</li>
  </ul>
  <ul class="abs footer-links" style="left:568px;top:96px">
    <li><svg width="8" height="8" viewBox="0 0 10 10"><path d="M3 1l4 4-4 4" fill="none" stroke="#fff" stroke-width="1.6"/></svg>Services</li>
    <li><svg width="8" height="8" viewBox="0 0 10 10"><path d="M3 1l4 4-4 4" fill="none" stroke="#fff" stroke-width="1.6"/></svg>Projects</li>
    <li><svg width="8" height="8" viewBox="0 0 10 10"><path d="M3 1l4 4-4 4" fill="none" stroke="#fff" stroke-width="1.6"/></svg>Our Blog</li>
    <li><svg width="8" height="8" viewBox="0 0 10 10"><path d="M3 1l4 4-4 4" fill="none" stroke="#fff" stroke-width="1.6"/></svg>Pages</li>
  </ul>

  <h4 class="abs footer-title" style="left:780px;top:50px">OUR OFFICE</h4>
  <ul class="abs office" style="left:780px;top:96px">
    <li><svg width="12" height="14" viewBox="0 0 12 16"><path d="M6 0a6 6 0 0 0-6 6c0 4.5 6 10 6 10s6-5.5 6-10a6 6 0 0 0-6-6zm0 8.5A2.5 2.5 0 1 1 6 3.5a2.5 2.5 0 0 1 0 5z" fill="#3176b5"/></svg>12 Meadow Lane, Warrington, UK</li>
    <li><svg width="12" height="12" viewBox="0 0 24 24"><path fill="#3176b5" d="M6.6 10.8a15 15 0 0 0 6.6 6.6l2.2-2.2a1 1 0 0 1 1-.25 11.4 11.4 0 0 0 3.6.6 1 1 0 0 1 1 1V20a1 1 0 0 1-1 1A17 17 0 0 1 3 4a1 1 0 0 1 1-1h3.5a1 1 0 0 1 1 1c0 1.25.2 2.45.6 3.6a1 1 0 0 1-.25 1z"/></svg>(01925) 555 0181</li>
    <li><svg width="13" height="10" viewBox="0 0 16 12"><rect x="0.5" y="0.5" width="15" height="11" fill="none" stroke="#3176b5"/><path d="M1 1l7 6 7-6" fill="none" stroke="#3176b5"/></svg>info@brightmeadow.example</li>
    <li><svg width="12" height="12" viewBox="0 0 24 24"><path fill="#3176b5" d="M6.6 10.8a15 15 0 0 0 6.6 6.6l2.2-2.2a1 1 0 0 1 1-.25 11.4 11.4 0 0 0 3.6.6 1 1 0 0 1 1 1V20a1 1 0 0 1-1 1A17 17 0 0 1 3 4a1 1 0 0 1 1-1h3.5a1 1 0 0 1 1 1c0 1.25.2 2.45.6 3.6a1 1 0 0 1-.25 1z"/></svg>(01925) 555 0199</li>
    <li><svg width="12" height="12" viewBox="0 0 16 16"><circle cx="8" cy="8" r="7" fill="none" stroke="#3176b5" stroke-width="1.5"/><path d="M8 4v4l3 2" fill="none" stroke="#3176b5" stroke-width="1.5"/></svg>Mon - Sat 9:00 - 18:00</li>
  </ul>
</footer>
<div class="abs copyright">© Copyright 2015 Bright Meadow. All rights reserved</div>

</body>
</html>
```